Tumbler Cafe - Menu Redesign

What We Want

We're looking for a bold redesign of our current menu. Our current menu is tired and boring and does not accurately reflect our revitalization of the Tumbler Cafe brand. Attachments will be submitted with the campaign for menu items.

Design Guidelines

• Creative use of typography and color. Think Bold, Fun, Loud and uninhibited.
• Fluid, easy to read, layout that emphasizes readability.
• The subtle, demure, look of typographic columns (examples below in resources)
• Creative use of 'wells' for menu item highlights as well as great boarders
• Loud typefaces as long as readability is the focus & emphasis.
• Small illustrations/icons but they must not effect or take the focus from the readability of the menu
• Big, oversized, menu that will look great on recycled paper
• Subtle watermarks/illustrations
• creative use of textures / highlights / section breaks

Menu Requirements

• 9”x12” paper size. Please notify us if your design works better in a different format.
• Oversized, designed for printing on recycled paper.
• Single Page Menu (use lunch on front and breakfast on back)
• Do not use $ or "..." in pricing. Please space all prices equally.
• Simplistic layout that emphasizes readability and logical navigation of menu items.
• Acceptable file types
• Photoshop
• Indesign
• illustrator
• Please contact us before you submit a design if you plan on using something else
• HTML/CSS would be a huge benefit. It's not a must, but it will definitely help you win the award.
• Must retain some of our current color scheme (red/orange/yellow – see attachments/website).

NOTE: Please download ALL attached resources for the project.
Updates

Current web site:  www.tumblercafe-example.com

please read attachment:  tumbler_menu_redesign_request.docx

Lots of good information & examples on menus we like and the design elements featured in the menu.

All,

Thanks for your design submissions!  With all the designs that have be submitted so far, we are confident that our money will be well spent.  I have changed the project to non-refundable.  Please continue working on your designs using the design_request doc that's posted for guidelines/requirements.  I will provide specific feedback to designs as needed.

For your convenience:

Design Guidelines

 

Creativeuse of typography and color.  Think Bold,Fun, Loud and uninhibited.

Fluid,easy to read, layout that emphasizes readability.

Thesubtle, demure, look of typographic columns (examples below in resources)

Creativeuse of 'wells' for menu item highlights as well as great boarders

Loudtypefaces as long as readability is the focus & emphasis.

Smallillustrations/icons but they must not effect or take the focus from thereadability of the menu

Big,oversized, menu that will look great on recycled paper

Subtlewatermarks/illustrations

creativeuse of textures / highlights / section breaks

 

  MenuRequirements

 

9”x12”paper size.  Please notify us if yourdesign works better in a different format.

Oversized,designed for printing on recycled paper.

SinglePage Menu (use lunch on front and breakfast on back)

Donot use $ or "..." in pricing.Please space all prices equally.

Simplisticlayout that emphasizes readability and logical navigation of menu items.

Acceptablefile types

Photoshop

Indesign

illustrator 

Pleasecontact us before you submit a design if you plan on using something else

HTML/CSSwould be a huge benefit.  It's not amust, but it will definitely help you win the award.

Mustretain some of our current color scheme (red/orange/yellow – seeattachments/website). 

 

Do Not Use

 

Skeuomorphismin any way.

Wedo not want any actual pictures of food on the menu (subtle illustrations /icons are great and encouraged).

Typefacesthat are hard to read.

Thanks!

dana

Reason: need to incorporate changes to menu / menu items

Please expect some new copy tonight (USA EST) for the breakfast menu items.  Thanks!

dana

COPY UPDATE:  Please check new menu item listing (revision 3) for updated copy.  Please revisit all menu items as I have grouped, consolidated, and eliminated some items.

Thanks!

dana 

DESIGN UPDATE:  I added an omelette hero/jumbotron design that we'd like to use to display the omelettes on the breakfast menu.  It doesn't have to be exactly like this one, it's just meant to be a guideline.  Please take a look and see if you can fit it in to your design.  Also, the copy has been updated for the breakfast & lunch menus.

Reason: Revised design changes not yet received.

Reason: Designer needs more tine to complete final submission. This will be the last extension. Thanks! dana

Target Market(s)

Women - 60% or more. Mostly professionals. 18-55.
Men - Professionals mostly. Judges, Attorneys, Agents, Ect. Ages 18-55.

Industry/Entity Type

Printing

Colors
f37022
ec1f27
f78f20
faa54b
f04a50
fee18a
faee3e

Requirements
Must have
• see menu requirements in task description.
Nice to have
• Design Ideas We Love

http://www.menugallery-example.com/menucraft/archives/stonegate_inn.php
We like: typefaces, typographic columns & layout, use of butcher-block print, simplicity
We don't like: lack of bold, color lack of textures, lack of general vitality in the brand, no use of icons/illustrations

http://www.menugallery-example.com/menucraft/archives/patty_vault.php
We like: typefaces, bold headers & section breaks, texturized typefaces, use of illustrations, and specifically we love how they did the 'custom creation' menu
We don't like: lack of bold color, lack of subtle texturing, little more use of illustrated icons would be nice

http://www.menugallery-example.com/menucraft/archives/the_rowdy_roost.php
We like: use of bold colors, organization & layout, the section highlights are nice
We don't like: lack of textures, lack subtle illustrations/icons.

http://www.menugallery-example.com/menucraft/archives/wexford_mill.php
We like: use of textures, typefaces, layout & organization, single page menu
We don't like: lack of textures, lack of bold color, lack of icons and menu item hightlights

http://www.menugallery-example.com/menucraft/archives/zibbo_caf.php
We like: use of texturing, typesfaces, layout & organization, creative use of illustrations/icons, bold colors
We don't like: not a huge fan of the bordering; and illustrations take up too much room for single page menu

http://www.menugallery-example.com/menucraft/archives/ved_hjornet_af_torvet.php
We like: creative use of typefaces, organization & layout, cool illustrations, oversized menu, section seperators are cool & unique
We don't like: lack of textures, menu items inside illustrations, typefaces can get hard to read in certain areas
Should not have
• Do Not Use

• Skeuomorphism in any way.
• We do not want any actual pictures of food on the menu (subtle illustrations / icons are great and encouraged).
• Typefaces that are hard to read.

```html
<!DOCTYPE html>
<html lang="en">
<head>
<meta charset="utf-8">
<title>Tumbler Cafe Menu</title>
<link href="https://fonts.googleapis.com/css2?family=Oswald:wght@400;500&family=Pathway+Gothic+One&display=swap" rel="stylesheet">
<style>
:root{
  --red:#c01f2e;
  --gold:#f7a21b;
  --paper:#ffffff;
  --ink:#111111;
  --art-dark:#1a1a1a;
  --art-mid:#4a4a4a;
  --art-light:#cfcfcf;
}
*{margin:0;padding:0;box-sizing:border-box}
html,body{width:900px;height:1200px;overflow:hidden;background:var(--paper)}
.menu{position:relative;width:900px;height:1200px;background:var(--red);color:var(--ink);font-family:"Pathway Gothic One",sans-serif}
.panel{position:absolute;top:0;height:1200px;background:var(--paper)}
.panel--lunch{left:19px;width:404px}
.panel--breakfast{left:455px;width:428px}
.divider-stripe{position:absolute;left:431px;top:0;width:12px;height:1200px;background:var(--gold)}
.art{position:absolute;border-radius:8px 8px 4px 4px;background:linear-gradient(180deg,var(--art-mid),var(--art-dark))}
.art--glass{background:linear-gradient(180deg,var(--art-light),var(--art-mid))}
.section{position:absolute}
.section-title{font-family:"Oswald",sans-serif;font-weight:400;font-size:21px;line-height:24px;text-transform:uppercase}
.item-list{list-style:none;font-size:10px}
.item-name{font-variant:small-caps;font-size:12.5px;letter-spacing:.3px}
.lunch .item-list{line-height:15.6px}
.kids .item-list{line-height:14.6px}
.breakfast .item-list{line-height:15.1px}
.sides{list-style:none;font-variant:small-caps;font-size:14.5px;line-height:20px}
.sides .small{font-variant:normal;font-size:11px;line-height:18px}
.sides .big{font-size:16px}
.note{font-size:9.5px}
</style>
</head>
<body>
<div class="menu">
  <div class="panel panel--lunch"></div>
  <div class="divider-stripe"></div>
  <div class="panel panel--breakfast"></div>

  <div class="art" role="img" aria-label="Salt and pepper shaker illustration" style="left:192px;top:12px;width:66px;height:82px"></div>
  <div class="art" role="img" aria-label="Pair of condiment bottles illustration" style="left:626px;top:18px;width:76px;height:80px"></div>
  <div class="art art--glass" role="img" aria-label="Glass salt and pepper shakers illustration" style="left:178px;top:1094px;width:80px;height:96px"></div>
  <div class="art" role="img" aria-label="Syrup jar and sugar dispenser illustration" style="left:654px;top:1076px;width:96px;height:112px"></div>

  <section class="section lunch" style="left:42px;top:132px;width:378px">
    <h2 class="section-title">Salads</h2>
    <ul class="item-list">
      <li class="item-name">The Venetian</li>
      <li>Homemade chicken or tuna salad tossed with romaine lettuce, tomatoes, carrots, onions,</li>
      <li>hot peppers, mushrooms and herbed oil &amp; vinegar</li>
      <li>Small 5.95 / Large 7.95</li>
      <li class="item-name">C.O.S</li>
      <li>Our delicious marinated chicken, grilled to tender perfection, served over a big romaine</li>
      <li>garden salad with our homemade caesar dijon dressing</li>
      <li>Small 5.95 / Large 7.95</li>
      <li class="item-name">Chef Salad</li>
      <li>Ham, Turkey &amp; Cheese over a Romaine Garden Mix with your choice of homemade dressing</li>
      <li>Small 5.95 / Large 8.95</li>
      <li class="item-name">The Combo</li>
      <li>Our Chicken, Tuna, and Egg Salad served over a big romaine garden salad, and our</li>
      <li>herbed oil and vinaigrette dressing on the side</li>
      <li>any two (2) 7.95</li>
      <li>any three (3) 8.95</li>
      <li class="item-name">Pear Gorgonzola Salad</li>
      <li>Fresh Pears and Crumbled Gorgonzola Cheese over a romaine medley, grilled spicy chicken</li>
      <li>marinated in our own spicy blend, chopped walnuts,</li>
      <li>and our fresh herbed oil and vinaigrette dressing</li>
      <li>Small 5.95 / Large 7.95</li>
      <li class="item-name">Greek Salad</li>
      <li>grilled lemon chicken, feta cheese, greek olives, chopped red onion and our</li>
      <li>Greek vinaigrette over a Romaine medley</li>
      <li>Small 5.95 / Large 7.95</li>
      <li class="item-name">Buffalo Chicken Salad</li>
      <li>grilled buffalo chicken, romaine medley, monterey jack cheese, tomatoes, croutons</li>
      <li>and red onion with crumbled blue cheese dressing</li>
      <li>Small 5.95 / Large 7.95</li>
      <li class="item-name">Ceasar Salad</li>
      <li>grilled spicy chicken over a romaine medley and our fresh caesar dressing</li>
      <li>small 5.95 / Large 7.95</li>
      <li>Spinach Salad 6.75</li>
      <li>chopped hard-boiled egg, bacon bits, red onion, carrots, mushroom and our</li>
      <li>fresh herbed oil and vinaigrette dressing</li>
      <li>with grilled chicken 8.75</li>
      <li class="item-name">Southwest Salad &nbsp;7.95</li>
      <li>fresh romaine medley, tomatoes, mexican corn, crushed tortilla chips, monterey jack</li>
      <li>cheese, black beans and sliced avocados topped</li>
      <li>with our fresh chipotle ranch dressing</li>
      <li>with spicy chicken 9</li>
      <li>with spicy skirt steak 10</li>
    </ul>
  </section>

  <section class="section kids" style="left:42px;top:834px;width:378px">
    <h2 class="section-title">Kids Menu</h2>
    <p class="note" style="margin-bottom:14px">Children 10 or under. Served with a bag of Crunchwell chips</p>
    <ul class="item-list">
      <li class="item-name">Grilled Cheese &nbsp;4</li>
      <li class="item-name">Chicken Nuggets &nbsp;4</li>
      <li class="item-name">Cheese Quesadilla &nbsp;4.50</li>
      <li>grilled flour tortilla with your choice of cheese</li>
      <li>with chicken or steak 6</li>
      <li class="item-name">Cheeseburger &nbsp;4.50</li>
      <li>4 oz prime beef, lettuce, tomato, red onion, side, and your choice of cheese</li>
      <li class="item-name">Kids Fajitas &nbsp;6</li>
      <li>Marinated chicken or steak, sauteed peppers, caramelized onions, and sour cream on the side</li>
      <li>with homemade guacamole 7</li>
    </ul>
    <p class="note" style="margin-top:16px">Please check specials menu for our list of seasonal creations</p>
  </section>

  <section class="section breakfast" style="left:506px;top:152px;width:370px">
    <h2 class="section-title">Breakfast</h2>
    <ul class="item-list">
      <li class="item-name">Eggs, Taters and Toast &nbsp;5.50</li>
      <li>Egg Whites Add 1.50</li>
      <li class="item-name">Egg Sandwich &nbsp;2.50</li>
      <li>Two egg Sandwich 3.50</li>
      <li class="item-name">Egg and Cheese Sandwich &nbsp;3.00</li>
      <li>Two egg and cheese sandwich 4.00</li>
      <li class="item-name">Meat, Egg, and Cheese Sandwich &nbsp;4.75</li>
      <li>In a bagel or wrap Add .50</li>
      <li class="item-name">Egg, Cheese and Veggie Sandwich &nbsp;4.75</li>
      <li class="item-name">Cheese Omelet with Taters and Toast &nbsp;6.50</li>
      <li>Add Veggies: (mushrooms, tomatoes, onion, broccoli, spinach, peppers, jalapenos)</li>
      <li>Add .50 each &nbsp;&nbsp;&nbsp; Egg whites Add 1.50</li>
      <li class="item-name">Breakfast Burrito</li>
      <li>Large Flour Tortilla filled with Scrambled Eggs, bacon, black beans</li>
      <li>Home fries, cheddar cheese, and our homemade salsa &nbsp;&nbsp; 5.95</li>
      <li class="item-name">South West White Veggie Omelet</li>
      <li>Four egg whites with Monterey jack cheese, Tomatoes, Onions, peppers,</li>
      <li>Spinach and our homemade salsa served with sliced tomatoes and toast 10.95</li>
      <li class="item-name">Hasta La Feasta</li>
      <li>Scrambled eggs in tortillas topped with melted cheese and</li>
      <li>our homemade salsa served with home fries 7.95</li>
      <li class="item-name">Grecian Omelet</li>
      <li>Spinach and Feta Omelet with taters and toast 8.95</li>
      <li class="item-name">Hunters Omelet</li>
      <li>Bacon, Potato, Onions and Cheddar Omelet w/ taters &amp; toast 8.95</li>
      <li class="item-name">Fruity French Pig Omelet</li>
      <li>Ham, Brie &amp; Raspberry jam Omelet w/ taters &amp; toast 8.95</li>
      <li class="item-name">Western Omelet</li>
      <li>Ham, Cheddar, pepper and onion Omelet w/ taters &amp; toast 8.95</li>
      <li class="item-name">Glutton's Paradise</li>
      <li>3 eggs your way, 2 pancakes and 3 (meats) of your choice 8.95</li>
    </ul>
  </section>

  <section class="section breakfast" style="left:506px;top:670px;width:370px">
    <ul class="sides">
      <li>Buttermilk Pancakes</li>
      <li class="small">(3) 5.25 &nbsp;Short Stack Buttermilk Pancakes (2) 4.25</li>
      <li class="big">French Toast (4) &nbsp;5.50</li>
      <li class="small">Short Stack French Toast (3) 4.50</li>
      <li class="small">Upgrade to 100% Maple Syrup &nbsp;1.50</li>
      <li style="margin-top:24px">Hog's Crown Bacon, Meadowvale Turkey Bacon, Sausage,</li>
      <li>Turkey Sausage, Tanner's Pork Roll or Ham Slice &nbsp;2.75</li>
      <li>Side of Home fries &nbsp;2.00</li>
      <li>Side of Eggs &nbsp;2.50</li>
      <li>Big English Muffin &nbsp;1.25</li>
      <li>Toast &nbsp;1.25</li>
      <li>Grilled Yogurt Muffin &nbsp;1.75</li>
      <li>Toasted Bagel &nbsp;1.50</li>
      <li>Toasted Bagel with cream cheese &nbsp;2.00</li>
      <li style="margin-top:28px">Homestead Oatmeal with brown sugar and milk &nbsp;3.00</li>
      <li class="small">with raisins 3.50 &nbsp;with fruit 4.50</li>
      <li>Quinoa with raisins and fruit &nbsp;5.00</li>
    </ul>
  </section>
</div>
</body>
</html>
```